Business Stationary
Business Cards and Letterheads
Professional
Dorian Hesketh
Principal/ Creative Director
12 Marrowfield Street
St. James
Trinidad and Tobago
plumvoraxialmarketing@brindlepost.com
I am now looking for Business Cards and stationary that reflect my company's intent to be distinctive....

```html
<!DOCTYPE html>
<html lang="en">
<head>
<meta charset="utf-8">
<title>PlumVorAxial Marketing Services – Business Card</title>
<link rel="stylesheet" href="https://fonts.googleapis.com/css2?family=Open+Sans:wght@400;600;700&display=swap">
<style>
  :root {
    --page-bg: #efe9df;
    --card-bg: #ffffff;
    --navy: #1f2a86;
    --blue-deep: #18206e;
    --blue-bright: #3c54c8;
    --grey-band: #9a9a9e;
    --grey-text: #8a8a8e;
    --ink: #2b2b2b;
  }
  html, body {
    margin: 0;
    padding: 0;
    width: 1200px;
    height: 931px;
    overflow: hidden;
    background: var(--page-bg);
    font-family: "Open Sans", Arial, sans-serif;
  }
  .business-card {
    position: absolute;
    left: 150px;
    top: 208px;
    width: 900px;
    height: 514px;
    background: var(--card-bg);
    border-radius: 40px;
    overflow: hidden;
    box-shadow: 0 10px 28px rgba(0,0,0,0.18);
  }
  .brand {
    position: absolute;
    left: 0;
    right: 0;
    top: 46px;
    text-align: center;
    color: var(--navy);
    font-weight: 700;
  }
  .brand-mark {
    display: block;
    margin: 0 auto 18px;
    width: 74px;
    height: 74px;
    border-radius: 50%;
    background: var(--navy);
  }
  .brand-name {
    font-size: 58px;
    line-height: 1;
    letter-spacing: 1px;
  }
  .brand-tagline {
    font-size: 26px;
    letter-spacing: 6px;
    text-transform: uppercase;
    margin-top: 6px;
  }
  .person {
    position: absolute;
    right: 525px;
    top: 322px;
    text-align: right;
  }
  .person-name {
    color: var(--navy);
    font-weight: 700;
    font-size: 25px;
  }
  .person-title {
    color: var(--ink);
    font-size: 16px;
    font-weight: 600;
    margin-top: 2px;
  }
  .contact {
    position: absolute;
    left: 410px;
    top: 262px;
    color: var(--grey-text);
    font-size: 17px;
    line-height: 23px;
  }
  .contact-label {
    color: var(--navy);
    font-weight: 700;
  }
  .card-band {
    position: absolute;
    left: 0;
    bottom: 0;
    width: 900px;
    height: 110px;
  }
</style>
</head>
<body>
  <div class="business-card">
    <div class="brand">
      <span class="brand-mark"></span>
      <div class="brand-name">PlumVorAxial</div>
      <div class="brand-tagline">Marketing Services</div>
    </div>

    <div class="person">
      <div class="person-name">Dorian Hesketh</div>
      <div class="person-title">Principal/ Creative Director</div>
    </div>

    <div class="contact">
      <div>12 Marrowfield Street</div>
      <div>St. James</div>
      <div>Trinidad and Tobago</div>
      <div><span class="contact-label">Cell :</span> (868) 555-0192</div>
      <div><span class="contact-label">Email :</span> plumvoraxialmarketing@brindlepost.com</div>
    </div>

    <svg class="card-band" viewBox="0 0 900 110" preserveAspectRatio="none" aria-hidden="true">
      <defs>
        <linearGradient id="bandBlue" x1="0" y1="0" x2="1" y2="0">
          <stop offset="0" stop-color="var(--blue-deep)"/>
          <stop offset="0.55" stop-color="var(--navy)"/>
          <stop offset="1" stop-color="var(--blue-bright)"/>
        </linearGradient>
      </defs>
      <path d="M380 58 C560 30 760 10 900 0 L900 110 L360 110 Z" fill="var(--grey-band)"/>
      <path d="M0 76 C180 80 360 70 560 40 C520 70 470 95 430 110 L0 110 Z" fill="url(#bandBlue)"/>
    </svg>
  </div>
</body>
</html>
```